Need designers to make a boring check list funky and fun

We are an executive rental company based in Sydney. We deal in fully furnished properties for both short and long term bookings. We have a check list for home owners to help them prepare their home for guests.
We are looking for an interesting design which makes the mundane tasks seem both fun and enjoyable.
Target Market(s)
single, couples and families where they are dual income households. Highly educated, high powered jobs with little to no time and are stressed needing a break, but also needing to pay the mortgage.
Industry/Entity Type
It Company
Colors
Designer to choose colors to be used in the design.
Requirements
Must have
- images of house rooms, clean.
- our logo on it
Nice to have
- icons for each section ie person swimming for a pool
Should not have
- just text no images

```html
<!DOCTYPE html>
<html lang="en">
<head>
<meta charset="utf-8">
<title>Checklist for Holiday Owners – Corella Properties</title>
<link rel="stylesheet" href="https://fonts.googleapis.com/css2?family=Roboto+Condensed:wght@300;400&family=Roboto:wght@900&family=Open+Sans:ital,wght@1,700&family=Raleway:wght@500&display=swap">
<style>
  :root{
    --paper:#efefef;
    --paper-deep:#e2e2e2;
    --general:#d3184a;
    --living:#6b1a1f;
    --kitchen:#2e2e2e;
    --bedroom:#1b3f6e;
    --pool:#1a86c7;
    --stairs:#e01b24;
    --band:#d81e4c;
    --brand-grey:#4a4a4a;
    --ink:#2a1212;
  }
  *{box-sizing:border-box;margin:0;padding:0}
  html,body{width:1131px;height:1200px;overflow:hidden;background:var(--paper)}
  .sheet{
    position:relative;width:1131px;height:1200px;overflow:hidden;
    background:radial-gradient(ellipse at 50% 85%, var(--paper-deep) 0%, var(--paper) 60%);
    font-family:"Roboto Condensed",sans-serif;
  }
  /* header */
  .brand{position:absolute;left:63px;top:42px;display:flex;align-items:center;gap:16px}
  .brand-dot{width:34px;height:34px;border-radius:50%;background:var(--general)}
  .brand-name{font-family:"Raleway",sans-serif;font-weight:500;font-size:26px;letter-spacing:3px;color:var(--brand-grey);line-height:30px}
  .brand-tagline{font-family:"Raleway",sans-serif;font-weight:500;font-size:14px;letter-spacing:2px;color:var(--general);margin-top:4px}
  .doc-title{position:absolute;left:618px;top:46px;width:452px;border-top:2px solid var(--general);padding-top:10px;text-align:right;font-family:"Open Sans",sans-serif;font-style:italic;font-weight:700;font-size:23px;letter-spacing:2px;color:var(--ink)}

  /* cards */
  .card{position:absolute;border:3px solid var(--c);border-radius:30px;padding:0 10px 12px 14px;color:var(--c)}
  .card-photo{position:absolute;left:50%;top:-78px;width:156px;height:156px;margin-left:-78px;border-radius:50%;border:8px solid var(--paper)}
  .card-title{font-family:"Roboto",sans-serif;font-weight:900;font-size:32px;text-align:center;margin-top:86px;margin-bottom:14px}
  .checklist{list-style:none}
  .checklist li{display:flex;align-items:center;gap:12px;font-size:13px;line-height:15px;text-transform:uppercase;margin-bottom:11px}
  .checklist li::before{content:"";flex:0 0 18px;height:18px;border:2px solid var(--c);border-radius:3px}
  .card--general{--c:var(--general);left:66px;top:183px;width:301px;height:584px}
  .card--living{--c:var(--living);left:423px;top:183px;width:300px;height:602px}
  .card--living .checklist li,.card--kitchen .checklist li,.card--bedroom .checklist li{color:#3a2a2a}
  .card--kitchen{--c:var(--kitchen);left:772px;top:183px;width:300px;height:663px}
  .card--kitchen .checklist li{margin-bottom:9px}
  .card--bedroom{--c:var(--bedroom);left:66px;top:850px;width:301px;height:301px;border-bottom:none;border-radius:30px 30px 0 0}
  .card--bedroom .card-title{margin-top:76px;margin-bottom:12px}
  .card--bedroom .checklist li{margin-bottom:9px}
  .card--pool{--c:var(--pool);left:419px;top:864px;width:301px;height:252px}
  .card--pool .card-title{margin-top:76px}
  .card--stairs{--c:var(--stairs);left:770px;top:926px;width:299px;height:190px}
  .card--stairs .card-photo{top:-100px}
  .card--stairs .card-title{margin-top:58px;margin-bottom:10px}
  .card--stairs .checklist li{margin-bottom:8px}

  .photo-house{background:radial-gradient(circle at 45% 40%,#c9382f 0%,#e9e4dc 55%,#f4f2ee 100%)}
  .photo-living{background:radial-gradient(circle at 50% 60%,#d98a2c 0%,#e7d9c5 55%,#f1ede6 100%)}
  .photo-kitchen{background:linear-gradient(160deg,#8a8580 0%,#3b3a38 45%,#cfc9c2 100%)}
  .photo-bedroom{background:linear-gradient(170deg,#cbb89a 0%,#8c7a62 55%,#5d5148 100%)}
  .photo-pool{background:linear-gradient(180deg,#2f8fc0 0%,#7cc3dd 40%,#b8241f 70%,#c9b8a4 100%)}
  .photo-stairs{background:linear-gradient(140deg,#e23b3b 0%,#1d2a6b 50%,#dfe3ec 100%)}

  /* footer band */
  .footer-band{position:absolute;left:0;bottom:0;width:1131px;height:49px;background:var(--band);display:flex;align-items:center;gap:14px;padding-left:63px}
  .footer-dot{width:16px;height:16px;border-radius:50%;background:#fff}
  .footer-name{font-family:"Raleway",sans-serif;font-weight:500;font-size:17px;letter-spacing:3px;color:#fff}
</style>
</head>
<body>
<main class="sheet">
  <header>
    <div class="brand">
      <span class="brand-dot"></span>
      <div>
        <div class="brand-name">CORELLA PROPERTIES</div>
        <div class="brand-tagline">STAYS MADE SIMPLE</div>
      </div>
    </div>
    <h1 class="doc-title">Checklist for Holiday Owners</h1>
  </header>

  <section class="card card--general">
    <div class="card-photo photo-house" role="img" aria-label="Small red-roofed house under a magnifying glass"></div>
    <h2 class="card-title">General</h2>
    <ul class="checklist">
      <li>Provide spare light bulbs and batteries for all the remotes</li>
      <li>Put felt pads under furniture to protect the floor from scratching</li>
      <li>Put coasters under any furniture with wheels</li>
      <li>Remove any personal items such as photos, and sentimental items</li>
      <li>Lock up all linen including tea towels</li>
      <li>Unplug any home phones</li>
      <li>Leave modem in an area accessible by the guests.</li>
      <li>Network name and password to be on sticker on device</li>
      <li>Ensure internet is unlimited and the network name and password are provided to Corella Properties</li>
      <li>Property to be pest sprayed for cockroaches, and ants</li>
    </ul>
  </section>

  <section class="card card--living">
    <div class="card-photo photo-living" role="img" aria-label="Patterned orange armchair in a bright living room"></div>
    <h2 class="card-title">Living Room</h2>
    <ul class="checklist">
      <li>Check all furniture, rugs, carpet and floors have no rips, tears, stains and are in good condition.</li>
      <li>Wash/steam clean cushion covers.</li>
      <li>Steam clean any upholstery if it requires it.</li>
      <li>If you have an animal all carpet, upholstery and rugs will need to be steam cleaned prior to guests' arrival.</li>
      <li>Put in new batteries to all remotes, smoke alarms and other such devices.</li>
      <li>Detailed instructions on how to work all electronics (in guest handbook template we provide)</li>
      <li>Pack away any faulty electrical equipment.</li>
      <li>Log out of all devices and set up a guest password for Orchard TV, Reelbox and cable TV accounts. (Password to go in guests manual and a sticker to go on the device)</li>
    </ul>
  </section>

  <section class="card card--kitchen">
    <div class="card-photo photo-kitchen" role="img" aria-label="Modern kitchen with dark splashback and steel appliances"></div>
    <h2 class="card-title">Kitchen</h2>
    <ul class="checklist">
      <li>Empty pantry (spices, salt and pepper and unopened tins can remain if you don't mind guests using them).</li>
      <li>Thoroughly clean oven and microwave.</li>
      <li>Wipe out cupboards and ensure all hinges are in working order clean out fridge and freezer. Wipe all surfaces.</li>
      <li>Check all appliances are in working order and clean.</li>
      <li>Run dishwasher with a dishwashing cleaner in it. Fill up the rinse aid.</li>
      <li>Remove any alcohol.</li>
      <li>Remove any sentimental or expensive crockery items.</li>
      <li>Check all crockery is not chipped or damaged.</li>
      <li>Leave crockery and cutlery for twice the maximum number of guests.</li>
      <li>Think of getting a glass top to protect tables and cabinets especially if they are French polished.</li>
    </ul>
  </section>

  <section class="card card--bedroom">
    <div class="card-photo photo-bedroom" role="img" aria-label="Bedroom with a four-poster bed and ceiling fan"></div>
    <h2 class="card-title">Bedroom</h2>
    <ul class="checklist">
      <li>Clear ½ the robes for the guests to use in each of the bedrooms. Lock the sections you are using.</li>
      <li>Clear out draws and bedside tables.</li>
      <li>Leave new mattress protectors, pillow protectors for each pillow, doona's, doona protectors, extra blankets and pillows including all sofa beds and trundle beds.</li>
    </ul>
  </section>

  <section class="card card--pool">
    <div class="card-photo photo-pool" role="img" aria-label="Red lounge chair beside a blue swimming pool"></div>
    <h2 class="card-title">Pool</h2>
    <ul class="checklist">
      <li>Check pool is compliant with the council and obtain certificate.</li>
      <li>Organise regular pool cleaner.</li>
      <li>Leave detailed pool instructions (in guest handbook template provided)</li>
    </ul>
  </section>

  <section class="card card--stairs">
    <div class="card-photo photo-stairs" role="img" aria-label="Staircase with red railings and blue carpet"></div>
    <h2 class="card-title">Stairs</h2>
    <ul class="checklist">
      <li>Check the balustrade and railings are secure</li>
      <li>Repair any loose carpet</li>
    </ul>
  </section>

  <footer class="footer-band">
    <span class="footer-dot"></span>
    <span class="footer-name">CORELLA PROPERTIES</span>
  </footer>
</main>
</body>
</html>
```